Stationary and Business Card Design

We need a stationery design and a business card design for a non-profit economics development agency. Our website is growharborline.org. Our clients are Canadian government agencies and large Chinese company. We need the design to be professional and corporate.

Please see attached for our Power Point presentation. Please take design elements from our website and our ppt.

```html
<!DOCTYPE html>
<html lang="en">
<head>
<meta charset="utf-8">
<title>Harborline Growth Alliance — Stationery</title>
<link href="https://fonts.googleapis.com/css2?family=Montserrat:wght@400;500;700;800&display=swap" rel="stylesheet">
<style>
  :root{
    --bg:#efede8;
    --paper:#ffffff;
    --red:#e23a35;
    --red-deep:#9c1f1b;
    --red-dark:#7d1714;
    --ink:#3a3a3a;
    --ink-soft:#6b6b6b;
  }
  *{box-sizing:border-box;margin:0;padding:0}
  html,body{width:1200px;height:882px;overflow:hidden;background:var(--bg);font-family:"Montserrat",Arial,sans-serif;color:var(--ink)}
  .canvas{position:relative;width:1200px;height:882px}
  .sheet{position:absolute;background:var(--paper);box-shadow:0 1px 3px rgba(0,0,0,.18)}
  .brand{display:flex;align-items:center;gap:6px;font-weight:700;color:var(--ink);white-space:nowrap;line-height:1.05}
  .brand-mark{background:var(--red);flex:none}

  /* Letterhead */
  .letterhead{left:75px;top:98px;width:496px;height:702px}
  .letterhead .brand{position:absolute;left:0;right:0;top:60px;justify-content:center;font-size:12px}
  .letterhead .brand-mark{width:14px;height:14px}
  .letterhead-footer{position:absolute;left:0;right:0;top:683px;text-align:center;font-size:5.6px;color:var(--ink)}
  .letterhead-footer b{font-weight:700}
  .letterhead-band{position:absolute;left:0;right:0;bottom:0;height:5px;background:linear-gradient(90deg,var(--red-deep),var(--red) 50%,var(--red-deep))}

  /* Card back */
  .card-back{left:587px;top:401px;width:220px;height:122px;overflow:hidden;background:linear-gradient(120deg,var(--red-dark),var(--red-deep) 45%,#c23a2a)}
  .card-back svg{position:absolute;inset:0}
  .card-back .brand{position:absolute;right:18px;top:52px;color:#fff;font-size:12px}
  .card-back .brand-mark{background:#fff;width:10px;height:10px}
  .card-back-url{position:absolute;left:10px;bottom:7px;font-size:5.5px;color:rgba(255,255,255,.7)}

  /* Card front */
  .card-front{left:819px;top:401px;width:223px;height:122px}
  .card-front .brand{position:absolute;left:14px;top:14px;font-size:7px}
  .card-front .brand-mark{width:9px;height:9px}
  .card-person{position:absolute;left:15px;top:58px}
  .card-name{font-size:7px;font-weight:500}
  .card-role{font-size:5.5px;font-style:italic;color:var(--ink-soft);margin-top:2px}
  .card-contact{position:absolute;left:117px;top:58px;font-size:5.2px;line-height:1.55}
  .card-contact p+p{margin-top:4px}

  /* Envelope */
  .envelope{left:587px;top:537px;width:526px;height:263px;overflow:hidden}
  .envelope .brand{position:absolute;left:18px;top:38px;font-size:10px}
  .envelope .brand-mark{width:12px;height:12px}
  .envelope-contact{position:absolute;left:188px;top:14px;font-size:5.2px;color:var(--ink);white-space:nowrap}
  .envelope-contact b{font-weight:700}
  .envelope-ribbon{position:absolute;left:0;top:62px;width:526px;height:62px;background:linear-gradient(90deg,rgba(226,58,53,.28),rgba(226,58,53,.12) 50%,rgba(156,31,27,.3))}
</style>
</head>
<body>
<main class="canvas">

  <section class="sheet letterhead" aria-label="Letterhead">
    <div class="brand"><span class="brand-mark"></span>Harborline Growth Alliance</div>
    <p class="letterhead-footer"><b>T</b> 416 555 0147 &nbsp;•&nbsp; <b>F</b> 416 555 0142 &nbsp;•&nbsp; 250 Maple Crest Rd., Suite 410, Markham, Ontario, L4C 2K9 &nbsp;•&nbsp; growharborline.org</p>
    <div class="letterhead-band"></div>
  </section>

  <section class="sheet card-back" aria-label="Business card back">
    <svg viewBox="0 0 220 122" preserveAspectRatio="none" aria-hidden="true">
      <path d="M0 0 H22 Q14 60 8 122 H0Z" fill="#b52a24" opacity=".55"/>
      <path d="M30 0 H70 Q52 60 40 122 H16 Q24 60 30 0Z" fill="#c8352c" opacity=".35"/>
      <path d="M90 0 H130 Q110 60 98 122 H70 Q82 60 90 0Z" fill="#d8463a" opacity=".25"/>
      <path d="M150 0 H220 V122 H140 Q150 60 150 0Z" fill="#d4513a" opacity=".3"/>
    </svg>
    <div class="brand"><span class="brand-mark"></span>Harborline</div>
    <p class="card-back-url">growharborline.org</p>
  </section>

  <section class="sheet card-front" aria-label="Business card front">
    <div class="brand"><span class="brand-mark"></span>Harborline Growth Alliance</div>
    <div class="card-person">
      <p class="card-name">Mara Ellison</p>
      <p class="card-role">Position</p>
    </div>
    <div class="card-contact">
      <p>250 Maple Crest Rd., Suite 410<br>Markham, Ontario, L4C 2K9</p>
      <p>T 416 555 0142<br>F 416 555 0147</p>
      <p>name@growharborline.org</p>
    </div>
  </section>

  <section class="sheet envelope" aria-label="Envelope">
    <div class="brand"><span class="brand-mark"></span>Harborline Growth Alliance</div>
    <p class="envelope-contact"><b>T</b> 416 555 0147 &nbsp;•&nbsp; <b>F</b> 416 555 0142 &nbsp;•&nbsp; 250 Maple Crest Rd., Suite 410, Markham, Ontario, L4C 2K9 &nbsp;•&nbsp; growharborline.org</p>
    <div class="envelope-ribbon" role="img" aria-label="Red and white ribbon ornament sweeping across the envelope"></div>
  </section>

</main>
</body>
</html>
```